The Ember Lantern

Look for someone who can add some splash and make this powerpoint presentation more dynamic. Feel free to use color, animations etc to provide some punch.

```html
<!DOCTYPE html>
<html lang="en">
<head>
<meta charset="utf-8">
<title>The Ember Lantern – Course Slides</title>
<link href="https://fonts.googleapis.com/css2?family=Barlow:wght@400;500;600;700&family=Barlow+Condensed:wght@400;600;700&display=swap" rel="stylesheet">
<style>
:root{
  --backdrop:#d5eafc;
  --ink:#000;
  --paper:#fff;
  --text:#1a1a1a;
  --rule:#333;
  --photo-a:#5a5148;
  --photo-b:#1f1c1a;
}
*{box-sizing:border-box;margin:0;padding:0}
html,body{width:1061px;height:1200px;overflow:hidden;background:var(--backdrop)}
body{position:relative;font-family:'Barlow',sans-serif;color:var(--text)}
.slide{position:absolute;width:454px;height:255px;background:var(--paper);overflow:hidden}
.col-l{left:63px}.col-r{left:539px}
.row-1{top:56px}.row-2{top:330px}.row-3{top:603px}.row-4{top:874px}
.abs{position:absolute}
.brand-mark{position:absolute;right:12px;top:10px;display:flex;align-items:center;gap:2px;font-family:'Barlow',sans-serif;font-weight:600;font-size:4px;letter-spacing:.3px;color:var(--ink)}
.brand-mark i{display:block;width:5px;height:5px;border-radius:50%;background:var(--ink)}
.footer-rule{position:absolute;left:22px;width:389px;top:239px;height:1px;background:var(--ink)}
.page-num{position:absolute;left:422px;top:232px;width:14px;height:14px;background:var(--ink);color:#fff;font-size:5px;font-weight:700;display:flex;align-items:center;justify-content:center}
.photo{position:absolute;background:radial-gradient(circle at 50% 45%,var(--photo-a),var(--photo-b))}
.tab{position:absolute;left:21px;top:0;width:56px;height:13px;background:var(--ink)}
ul.dots{list-style:none}
ul.dots li{position:relative;padding-left:11px;font-size:7.6px;line-height:10px}
ul.dots li::before{content:"•";position:absolute;left:2px}
.heading{font-family:'Barlow',sans-serif;font-size:16px;font-weight:400;color:var(--ink)}
.heading b{font-weight:700}

/* slide 1 */
.cover{background:var(--ink);color:#fff}
.cover .name{position:absolute;left:22px;top:92px;display:flex;align-items:center;gap:7px;font-family:'Barlow',sans-serif;font-weight:500;font-size:15px;letter-spacing:3px}
.cover .name i{display:block;width:9px;height:9px;background:#fff}
.cover .title{position:absolute;left:22px;top:170px;font-family:'Barlow Condensed',sans-serif;font-size:31px;line-height:1;letter-spacing:.3px;font-weight:400}
.cover .title b{font-weight:700}
.cover .sub{position:absolute;left:23px;top:206px;font-family:'Barlow Condensed',sans-serif;font-size:7px}
.cover .v-line{position:absolute;left:424px;top:135px;width:1px;height:107px;background:#fff}
.cover .h-line{position:absolute;left:332px;top:229px;width:107px;height:1px;background:#fff}
.cover .num{position:absolute;left:417px;top:241px;font-size:4px;color:#888}

/* agenda */
.module-box{position:absolute;left:21px;top:0;width:56px;height:77px;background:var(--ink);color:#fff}
.module-box .lbl,.module-box .no,
.section-bar .lbl,.section-bar .no{position:absolute;left:0;right:0;display:block;text-align:center}
.module-box .lbl{top:35px;font-weight:700;font-size:8px}
.module-box .no{top:46px;font-weight:700;font-size:20px;line-height:1}
.agenda-title{position:absolute;left:90px;top:49px;font-weight:700;font-size:14.5px;color:var(--ink)}
.agenda-col{position:absolute;top:107px;width:124px}
.agenda-col li{list-style:none;position:relative;padding-left:11px;font-size:7.6px;line-height:9.8px;color:var(--text)}
.agenda-col li::before{content:"•";position:absolute;left:2px}
.agenda-col .item{height:31px;border-bottom:1px solid var(--rule);padding-top:4px}
.agenda-col .item:nth-child(3){height:22px}
.agenda-col .item:last-child{border-bottom:none}

/* section */
.section-bar{position:absolute;left:21px;top:0;width:61px;height:225px;background:var(--ink);color:#fff}
.section-bar .lbl{top:128px;font-weight:700;font-size:8px}
.section-bar .no{top:140px;font-weight:700;font-size:20px;line-height:1}
.section-title{position:absolute;left:95px;top:122px;font-weight:700;font-size:28px;line-height:34px;color:var(--ink)}

/* about */
.band{position:absolute;left:0;width:454px;background:var(--ink)}
.cond-title{position:absolute;font-family:'Barlow Condensed',sans-serif;font-weight:700;color:var(--ink)}
.arrow-list{position:absolute;left:230px;top:81px;width:185px;list-style:none;color:#fff}
.arrow-list li{position:relative;padding-left:13px;font-size:7.6px;line-height:9.4px;margin-bottom:2.7px}
.arrow-list li::before{content:"➤";position:absolute;left:0;font-size:6px}

/* results */
.stat{position:absolute;width:161px;color:#fff;font-size:7.6px;line-height:10px;padding-bottom:6px}
.stat.ruled{border-bottom:1px solid #777}
.stat b{font-size:15px;font-weight:700}

/* audience */
.for-box{position:absolute;left:0;top:22px;width:235px;height:203px;background:var(--ink);color:#fff}
.for-box .cond-title{color:#fff;left:29px;top:13px;font-size:15px}
.for-box ul{position:absolute;left:29px;top:45px;width:190px}
.for-box li{margin-bottom:11px;line-height:10px}
.not-for .cond-title{left:255px;top:36px;font-size:15px}
.not-for ul{position:absolute;left:255px;top:68px}
.not-for li{margin-bottom:10.5px}
</style>
</head>
<body>

<section class="slide col-l row-1 cover">
  <div class="name"><i></i>LANTERN WORKS</div>
  <h1 class="title"><span>THE</span> <b>EMBER LANTERN</b></h1>
  <p class="sub">How to raise faster, get back to building and grow</p>
  <div class="v-line"></div>
  <div class="h-line"></div>
  <span class="num">1</span>
</section>

<section class="slide col-r row-1">
  <div class="brand-mark"><i></i>LANTERN WORKS</div>
  <div class="module-box"><span class="lbl">Module</span><span class="no">01</span></div>
  <h2 class="agenda-title">The Fundraising Journey</h2>
  <ul class="agenda-col" style="left:23px">
    <li class="item">Welcome</li>
    <li class="item">About Me &amp; My Background</li>
    <li class="item">Why I created this course</li>
    <li class="item">The Fundraising Journey</li>
  </ul>
  <ul class="agenda-col" style="left:160px">
    <li class="item">It’s All About The Story</li>
    <li class="item">Accelerators (Good/Bad/Maybe)</li>
    <li class="item">Why Not Cedar Row?</li>
    <li class="item">The different types of capital</li>
  </ul>
  <ul class="agenda-col" style="left:300px">
    <li class="item">Where to find the accredited investors?</li>
    <li class="item">Unlocking the Power of Angel Investors</li>
    <li class="item">Early-Stage Fundraising Traps</li>
    <li class="item">The Easiest Money You Will Ever Raise</li>
  </ul>
  <div class="footer-rule"></div><div class="page-num">2</div>
</section>

<section class="slide col-l row-2">
  <div class="brand-mark"><i></i>LANTERN WORKS</div>
  <div class="section-bar"><span class="lbl">Module</span><span class="no">01</span></div>
  <h2 class="section-title">The Fundraising<br>Journey</h2>
  <div class="footer-rule"></div><div class="page-num">3</div>
</section>

<section class="slide col-r row-2">
  <div class="brand-mark"><i></i>LANTERN WORKS</div>
  <div class="band" style="top:69px;height:134px"></div>
  <div class="photo" role="img" aria-label="Portrait photo of the course founder" style="left:24px;top:23px;width:180px;height:202px"></div>
  <h2 class="cond-title" style="left:228px;top:24px;font-size:17px">About Me &amp; My Background</h2>
  <ul class="arrow-list">
    <li>Over the last 25yrs, I helped two companies build business units to revenues over $1B annually.</li>
    <li>Then, in 2018, I burned out.</li>
    <li>So, I decided to leave the corporate executive grind to help early-stage founders.</li>
    <li>So, I started building my company and brand in 2018.</li>
    <li>Since that day, I’ve spent my time finding ways to help early-stage Founders win!</li>
  </ul>
  <div class="footer-rule"></div><div class="page-num">4</div>
</section>

<section class="slide col-l row-3">
  <div class="brand-mark"><i></i>LANTERN WORKS</div>
  <div class="band" style="top:69px;height:154px"></div>
  <div class="photo" role="img" aria-label="Small portrait photo of the course founder" style="left:24px;top:23px;width:65px;height:73px"></div>
  <h2 class="cond-title" style="left:103px;top:37px;font-size:16px">My Results</h2>
  <div class="stat ruled" style="left:34px;top:112px"><b>64</b> companies invested in</div>
  <div class="stat ruled" style="left:34px;top:148px"><b>35</b> companies have gotten to Series A</div>
  <div class="stat" style="left:34px;top:182px"><b>$1.08B+</b> capital raised by my portfolio companies</div>
  <div class="stat ruled" style="left:252px;top:112px"><b>8</b> exits to date</div>
  <div class="stat ruled" style="left:252px;top:150px">Consulting business working with early-stage founders across <strong>5</strong> continents</div>
  <div class="stat" style="left:252px;top:186px"><b>90%</b> margins</div>
  <div class="footer-rule" style="left:24px"></div><div class="page-num">5</div>
</section>

<section class="slide col-r row-3">
  <div class="brand-mark"><i></i>LANTERN WORKS</div>
  <div class="tab"></div>
  <h2 class="heading abs" style="left:22px;top:23px"><b>Why I Created</b> This Course</h2>
  <p class="abs" style="left:22px;top:57px;font-size:7.6px">Spent 6 years chatting with over 3,000 founders and learned:</p>
  <ul class="dots abs" style="left:22px;top:81px;width:400px">
    <li style="margin-bottom:3px">The fundraising process is NOT transparent</li>
    <li style="margin-bottom:3px">Founders don’t know where to begin, who to talk to or where to start</li>
    <li style="margin-bottom:3px">Founders don’t get the candid feedback they need</li>
    <li style="margin-bottom:3px">There is not easy way to find the right type of investors</li>
    <li style="margin-bottom:3px">Founders don’t always know what investors want, how to present it and the what the necessary KPI’s for success are</li>
    <li style="margin-bottom:3px">Founders underestimate how hard, long and tedious this process is start to finish</li>
    <li>The result is a fragmented, slow and challenging journey that leaves founders feeling empty and ultimately unfunded.</li>
  </ul>
  <div class="footer-rule"></div><div class="page-num">6</div>
</section>

<section class="slide col-l row-4">
  <div class="brand-mark"><i></i>LANTERN WORKS</div>
  <div class="tab"></div>
  <h2 class="heading abs" style="left:22px;top:23px"><b>Expected Results</b> For Founders</h2>
  <ul class="dots abs" style="left:22px;top:62px;width:400px">
    <li style="margin-bottom:3px">Founders now have a firm understanding of the fundraising process end-to-end</li>
    <li style="margin-bottom:3px">Founder have resources to help them find the right investors at the right time</li>
    <li style="margin-bottom:3px">Founders understand the different types of investors, motivation and stages</li>
    <li style="margin-bottom:3px">Founders understand how to tell their story more effectively</li>
    <li style="margin-bottom:3px">Founders feel equipped to successfully raise capital from the right type of investors</li>
    <li>Founders reduce to fundraise from 6-8 months to 3-6 mths</li>
  </ul>
  <div class="footer-rule"></div><div class="page-num">7</div>
</section>

<section class="slide col-r row-4">
  <div class="brand-mark"><i></i>LANTERN WORKS</div>
  <div class="for-box">
    <h2 class="cond-title">Who Is This Course for?</h2>
    <ul class="dots">
      <li>Early-Stage founders considering raising outside capital to fund their company.</li>
      <li>Founders looking to understand the fundraising process along with the players involved</li>
      <li>Founders who are looking to accelerate the capital raising process for their company.</li>
      <li>Founders who are looking to nail their ICP (Ideal Customer Profile) for investors</li>
      <li>Founders who are frustrated with how long and hard the fundraising process can be.</li>
    </ul>
  </div>
  <div class="not-for">
    <h2 class="cond-title">Who Isn’t This Course For?</h2>
    <ul class="dots">
      <li>Tire Kickers</li>
      <li>Wantrapreneurs vs Entrepreneurs</li>
      <li>Founders at Series A and beyond</li>
      <li>Founders who are not willing to do the work</li>
    </ul>
  </div>
  <div class="footer-rule"></div><div class="page-num">8</div>
</section>

</body>
</html>
```